Media/PR business needs a website upgrade

Modernise my website www.pvl.net.au into a simpler and mobile friendly site with the usual plugins, maximum 5 pages, 4 might be enough. My page is already hosted and I have an email address so I just want to work with a designer who is fantastic with WordPress, to refresh and simplify the 6 year-old look.

Target Market(s)

men & women 25-55

Industry/Entity Type

Business

Coding

Coded - Design and coding required

Number of Pages Required

4 page

Font styles to use
Sans Serif

Colors
f37122
ffffff

Requirements
Must have
• Social media plugins, about, client portfolio, contact (can be under about)blog capability
Nice to have
• photos of jobs I've done
Should not have
• e-commerce, can lose all the client logos

```html
<!DOCTYPE html>
<html lang="en">
<head>
<meta charset="utf-8">
<title>Pivot Line Media</title>
<link href="https://fonts.googleapis.com/css2?family=Oswald:wght@300;400&family=Roboto+Condensed:wght@300;400&display=swap" rel="stylesheet">
<style>
:root{
  --orange:#f37122;
  --orange-soft:#f7931e;
  --dark:#2f2f2f;
  --darker:#262626;
  --tab:#2b2b2b;
  --white:#ffffff;
  --grey-text:#4a4a4a;
  --nav-top:#8c8c8c;
  --nav-bottom:#6c6c6c;
}
*{box-sizing:border-box;margin:0;padding:0}
html,body{width:1200px;height:1200px;overflow:hidden}
body{background:var(--dark);font-family:"Roboto Condensed",Arial,sans-serif;color:var(--white);position:relative}
.abs{position:absolute}
.heading{font-family:"Oswald",Arial,sans-serif;font-weight:300}

/* header */
.brand{left:122px;top:13px;display:flex;align-items:center;gap:8px}
.brand-dot{width:56px;height:56px;border-radius:50%;background:var(--orange)}
.brand-name{font-size:14px;line-height:13px;color:var(--white)}
.phone{left:955px;top:26px;display:flex;align-items:center;gap:6px;font-size:19px;font-weight:300}
.phone-icon{width:33px;height:33px;border-radius:50%;background:#6a6a6a;display:flex;align-items:center;justify-content:center}

/* nav */
.nav{left:122px;top:89px;width:974px;height:55px;background:linear-gradient(var(--nav-top),var(--nav-bottom));}
.nav a{position:absolute;top:20px;font-size:12px;color:var(--white);text-decoration:none;text-transform:uppercase}
.nav .active{top:8px;left:12px;width:66px;height:40px;border:1px solid #9a9a9a;background:#777;text-align:center;line-height:38px}
.social{position:absolute;top:10px;width:35px;height:35px;border-radius:50%;background:#3a3a3a;border:2px solid #5a5a5a;font-size:10px;text-align:center;line-height:31px}

/* hero */
.hero-photo{left:122px;top:151px;width:219px;height:318px;background:linear-gradient(160deg,#c9b9a6,#8a8f9a 60%,#3b6fb3)}
.hero-title{left:341px;top:151px;width:399px;height:137px;background:var(--dark);padding:18px 28px 0}
.hero-title h1{font-family:"Oswald",Arial,sans-serif;font-weight:400;font-size:24px;line-height:25px;text-transform:uppercase;letter-spacing:-.2px}
.hero-title h1 .light{font-weight:300}
.hero-copy{left:341px;top:288px;width:399px;height:181px;background:var(--orange-soft);padding:17px 28px 0;font-size:11.4px;line-height:14.3px;font-weight:300;text-align:justify}
.hero-copy p{margin-bottom:10px}

/* social feed */
.feed{left:740px;top:151px;width:356px;height:318px;background:var(--white);color:var(--grey-text)}
.feed-cover{position:absolute;left:0;top:0;width:356px;height:137px;background:linear-gradient(135deg,#5d7fb0,#a9bcd4 55%,#3a5f95)}
.feed-avatar{position:absolute;width:50px;height:50px;background:linear-gradient(#d4b89a,#3e78c2);border:2px solid var(--white)}
.feed-page{position:absolute;left:78px;top:13px;font-family:"Oswald",Arial,sans-serif;font-size:17px;color:var(--white)}
.feed-likes{position:absolute;left:78px;top:33px;font-size:12px;color:var(--white)}
.feed-btn{position:absolute;top:100px;height:22px;background:var(--white);border:1px solid #ccc;font-size:11px;line-height:20px;padding:0 6px;color:#333}
.friends{position:absolute;left:16px;top:170px;display:flex;gap:2px}
.friends span{width:31px;height:28px;background:linear-gradient(#7d8a99,#3f4d5e)}
.feed-post-name{position:absolute;left:78px;top:220px;font-family:"Oswald",Arial,sans-serif;font-size:15px;color:#333}
.feed-square{position:absolute;left:330px;top:218px;width:16px;height:16px;background:#3b5998}
.feed-bar{position:absolute;right:0;top:137px;width:8px;height:76px;background:#c8c8c8}

/* about */
.about{left:122px;top:477px;width:331px;height:306px;background:var(--orange-soft)}
.tab{position:absolute;background:var(--tab);font-family:"Oswald",Arial,sans-serif;font-weight:300;font-size:18px;padding:0 11px;display:flex;align-items:flex-end;padding-bottom:8px}
.about-text{position:absolute;left:31px;top:66px;width:257px;height:210px;overflow:hidden;font-size:11.4px;line-height:14.3px;font-weight:300;text-align:justify}
.about-text p{margin-bottom:4px}
.scroll{position:absolute;width:5px;background:rgba(255,255,255,.35)}
.scroll i{display:block;width:5px;background:var(--white)}
.carousel{left:453px;top:477px;width:643px;height:306px;background:linear-gradient(180deg,#c9c6bf,#7c8a76 45%,#4a5a6a)}
.arrow{position:absolute;top:607px;width:30px;height:30px;border-radius:50%;background:var(--orange-soft)}
.dots{left:744px;top:757px;display:flex;gap:5px}
.dots i{width:11px;height:11px;border-radius:50%;background:#ddd}
.dots i:first-child{background:var(--orange-soft)}

/* services */
.services{left:122px;top:790px;width:974px;height:410px;background:var(--orange-soft);overflow:hidden}
.card{position:absolute;width:451px;height:224px;background:var(--white);color:var(--grey-text)}
.card-photo{position:absolute;left:0;top:0;width:176px;height:224px}
.card-num{position:absolute;left:176px;top:0;width:43px;height:44px;background:var(--tab);color:var(--white);font-family:"Oswald",Arial,sans-serif;font-weight:300;font-size:16px;text-align:center;line-height:44px}
.card-title{position:absolute;left:228px;top:11px;font-family:"Oswald",Arial,sans-serif;font-weight:300;font-size:17px;color:#222;text-transform:uppercase}
.card-body{position:absolute;left:190px;top:52px;width:238px;height:158px;overflow:hidden;font-size:11.4px;line-height:14.2px;font-weight:300;text-align:justify}
.card-body p{margin-bottom:10px}
.card .scroll{left:435px;top:54px;height:155px;background:#ddd}
.card .scroll i{background:#333;height:60px}
</style>
</head>
<body>

<header>
  <div class="abs brand">
    <div class="brand-dot"></div>
    <div class="brand-name">Pivot<br>Line<br>Media</div>
  </div>
  <div class="abs phone">
    <span class="phone-icon">
      <svg width="16" height="16" viewBox="0 0 24 24"><path fill="#2f2f2f" d="M6.6 10.8c1.4 2.8 3.8 5.1 6.6 6.6l2.2-2.2c.3-.3.7-.4 1-.2 1.1.4 2.3.6 3.6.6.6 0 1 .4 1 1V20c0 .6-.4 1-1 1C10.6 21 3 13.4 3 4c0-.6.4-1 1-1h3.5c.6 0 1 .4 1 1 0 1.3.2 2.5.6 3.6.1.3 0 .7-.2 1z"/></svg>
    </span>
    +61 400 555 210
  </div>
</header>

<nav class="abs nav">
  <a class="active" href="#">Home</a>
  <a href="#" style="left:98px">Projects / Event</a>
  <a href="#" style="left:233px">Client</a>
  <a href="#" style="left:309px">Testimonials</a>
  <a href="#" style="left:424px">Blog</a>
  <a href="#" style="left:491px">Contact</a>
  <span class="social" style="left:818px">Like</span>
  <span class="social" style="left:864px">Post</span>
  <span class="social" style="left:909px">Link</span>
</nav>

<section>
  <div class="abs hero-photo" role="img" aria-label="Portrait of founder Dana Whitlock in a sailing jacket"></div>
  <div class="abs hero-title">
    <h1><span class="light">Pivot Line Media is an</span><br>established specialist public<br>relations <span class="light">and</span> event<br>management business.</h1>
  </div>
  <div class="abs hero-copy">
    <p>With a communications degree and 20 plus years experience working in public relations, publicity, media and project management, PVL founder Dana Whitlock offers a complete contract based option for your next major sporting, social, cultural or community event.</p>
    <p>Contact Dana at PVL for strategic advice on sponsorship spend and how to leverage your investment, and to tap into her extensive media and professional network.</p>
    <p>Flexible, composed and relationship focused freelancer ready to start work.</p>
  </div>

  <aside class="abs feed">
    <div class="feed-cover" role="img" aria-label="Cover photo of yachts racing under colourful spinnakers"></div>
    <div class="feed-avatar" style="left:16px;top:14px" role="img" aria-label="Profile photo"></div>
    <div class="feed-page">PVL - Dana Whitlock</div>
    <div class="feed-likes">410 likes</div>
    <div class="feed-btn" style="left:18px">Like Page</div>
    <div class="feed-btn" style="right:14px">&#10150; Share</div>
    <div class="feed-bar"></div>
    <div style="position:absolute;left:16px;top:152px;font-size:10.5px">Be the first of your friends to like this</div>
    <div class="friends" role="img" aria-label="Friend profile photos"><span></span><span></span><span></span><span></span><span></span><span></span><span></span><span></span></div>
    <div class="feed-avatar" style="left:16px;top:210px;width:50px;height:48px;border:0" role="img" aria-label="Profile photo"></div>
    <div class="feed-post-name">PVL - Dana Whitlock</div>
    <div style="position:absolute;left:78px;top:240px;font-size:10.5px">7 hours ago</div>
    <div class="feed-square"></div>
    <p style="position:absolute;left:16px;top:266px;width:334px;font-size:10.3px;line-height:13px;text-align:justify">A great initiative by Global Sailing, looking forward to listening in to panel members Mia Corrin (left in pic) Tess Hardy Elena Varga &amp; I encourage all Australian yacht clubs to join the conversation</p>
  </aside>
</section>

<section>
  <div class="abs about">
    <div class="tab" style="left:28px;top:0;height:54px">ABOUT</div>
    <div class="about-text">
      <p>Dana grew up on Scotland Island in Pittwater on Sydney's northern beaches, the breeding ground for many Australian sailing greats including the Harlows, Prestons and the Kellys</p>
      <p>As a 'tinny terror' she attended Harbourview Public School then Bayside High School with some of these sailing families, and now through her work she's back mingling with the greats.</p>
      <p>A communications degree at Eastport University, a career that has seen her rise to the top of her specialist field and three children later has brought her full circle back to the island as a home owner.</p>
      <p>Sailing-wise the women's twilight at the Royal</p>
    </div>
    <div class="scroll" style="left:289px;top:70px;height:208px"><i style="height:80px"></i></div>
  </div>
  <div class="abs carousel" role="img" aria-label="Marina crowded with race yachts and event flags before the start"></div>
  <span class="arrow" style="left:471px"><svg width="30" height="30" viewBox="0 0 30 30"><path d="M17 9l-6 6 6 6" stroke="#fff" stroke-width="3" fill="none"/></svg></span>
  <span class="arrow" style="left:1047px"><svg width="30" height="30" viewBox="0 0 30 30"><path d="M13 9l6 6-6 6" stroke="#fff" stroke-width="3" fill="none"/></svg></span>
  <div class="abs dots"><i></i><i></i><i></i><i></i></div>
</section>

<section class="abs services">
  <div class="tab" style="left:28px;top:0;height:54px">SERVICES</div>

  <article class="card" style="left:28px;top:75px">
    <div class="card-photo" role="img" aria-label="Surf lifesavers racing boards into the waves" style="background:linear-gradient(#b9c4c9,#8c7a68 60%,#d9d9d9)"></div>
    <div class="card-num">01</div>
    <h3 class="card-title">Sports Media</h3>
    <div class="card-body">
      <p>PVL founder Dana Whitlock has worked closely with Australian and international sports media since 1996.</p>
      <p>Key events include the annual Coastal Sailing Cup - Port Bay, Festival of Sails, Harbour to Cape Yacht Race, Palm Island Race Week and Surf Rescue League state open titles.</p>
      <p>Dana has a thorough understanding of the media's requirements for a strong story angle.</p>
    </div>
    <div class="scroll"><i></i></div>
  </article>

  <article class="card" style="left:494px;top:75px">
    <div class="card-photo" role="img" aria-label="Yachts with spinnakers sailing past a waterfront pavilion" style="background:linear-gradient(#6d8fb8,#9fb6cc 55%,#4b4f55)"></div>
    <div class="card-num">02</div>
    <h3 class="card-title">Publicity</h3>
    <div class="card-body">
      <p>Generating media publicity for both the event and its sponsor is one of Dana's key strengths and drivers.</p>
      <p>She works with clients to establish objectives and target audiences then develops a PR/media plan to deliver on the brief. From long lead magazines and social media campaigns through to short lead opportunities, media attendance at the event and the resulting coverage, PVL will stay calm and within budget and step through the process.</p>
    </div>
    <div class="scroll"><i></i></div>
  </article>

  <article class="card" style="left:28px;top:316px">
    <div class="card-photo" role="img" aria-label="Racing catamaran crew on deck" style="background:linear-gradient(#9bb3c8,#c44 70%,#333)"></div>
    <div class="card-num">03</div>
    <h3 class="card-title">Sponsorship Leverage</h3>
    <div class="card-body">
      <p>Dana has worked with many sponsors including premium brand clients Meridian Watches, Kestrel Motors and Arden Cars.</p>
    </div>
    <div class="scroll"><i></i></div>
  </article>

  <article class="card" style="left:494px;top:316px">
    <div class="card-photo" role="img" aria-label="Crowd of spectators waving flags at an event" style="background:linear-gradient(#c86b5a,#8a6f66 60%,#d8d0c8)"></div>
    <div class="card-num">04</div>
    <h3 class="card-title">Event Management</h3>
    <div class="card-body">
      <p>From planning through to execution and follow up, PVL provides a complete service.</p>
    </div>
    <div class="scroll"><i></i></div>
  </article>
</section>

</body>
</html>
```